Business Cards and Stationery for a laboratory quality consulting business
Brennick Quality Solutions
Creative Brief
Simple
Marion Brennick
Principal Consultant
4817 Thistlewood Lane Cary, NC 27604
marion@brennickquality.example
www.brennickquality.example

```html
<!DOCTYPE html>
<html lang="en">
<head>
<meta charset="utf-8">
<title>Brennick Quality Solutions – Business Card</title>
<link href="https://fonts.googleapis.com/css2?family=Montserrat:wght@500;600;700;800&display=swap" rel="stylesheet">
<style>
  :root {
    --teal: #138d86;
    --orange: #f5a623;
    --ink: #4a4a4a;
    --card: #ffffff;
    --backdrop: #ececec;
  }
  * { margin: 0; padding: 0; box-sizing: border-box; }
  html, body { width: 1200px; height: 518px; overflow: hidden; }
  body {
    background: var(--backdrop);
    font-family: "Montserrat", Arial, sans-serif;
    position: relative;
  }
  .card {
    position: absolute;
    top: 149px;
    width: 458px;
    height: 230px;
    background: var(--card);
    overflow: hidden;
    box-shadow: 0 3px 10px rgba(0,0,0,0.12);
  }
  .card--front { left: 173px; }
  .card--back { left: 686px; }
  .card svg.decor { position: absolute; inset: 0; }

  .brand { position: absolute; display: flex; align-items: center; gap: 7px; }
  .brand__dot { width: 12px; height: 12px; border-radius: 50%; background: var(--orange); flex: none; }
  .brand__name {
    color: var(--teal); font-weight: 800; line-height: 1.05;
  }
  .card--front .brand { left: 22px; top: 24px; }
  .card--front .brand__name { font-size: 13px; width: 120px; }
  .card--back .brand { left: 50%; top: 50%; transform: translate(-50%, -50%); gap: 9px; }
  .card--back .brand__name { font-size: 17px; width: 160px; }

  .person { position: absolute; left: 300px; top: 30px; }
  .person__name { color: var(--orange); font-weight: 700; font-size: 14px; }
  .person__title { color: var(--teal); font-weight: 600; font-size: 9.5px; margin-top: 2px; }

  .contacts { position: absolute; left: 22px; top: 118px; list-style: none; }
  .contacts li {
    display: flex; align-items: center; gap: 7px;
    font-size: 8.5px; color: var(--ink); font-weight: 500;
    margin-bottom: 9px; line-height: 1.2;
  }
  .contacts .icon {
    width: 13px; height: 13px; border-radius: 50%; background: var(--orange);
    flex: none; display: flex; align-items: center; justify-content: center;
  }
</style>
</head>
<body>
  <section class="card card--front">
    <svg class="decor" width="458" height="230" viewBox="0 0 458 230">
      <path d="M320 230 C340 200 350 170 380 165 C410 160 420 130 458 118 L458 230 Z" fill="var(--orange)"/>
      <path d="M332 230 C352 205 362 182 390 177 C420 172 428 145 458 134 L458 230 Z" fill="var(--teal)"/>
    </svg>

    <div class="brand">
      <span class="brand__dot"></span>
      <span class="brand__name">Brennick Quality Solutions</span>
    </div>

    <div class="person">
      <p class="person__name">Marion Brennick</p>
      <p class="person__title">Principal Consultant</p>
    </div>

    <ul class="contacts">
      <li><span class="icon"><svg width="7" height="8" viewBox="0 0 7 8"><path d="M3.5 0a2.7 2.7 0 0 0-2.7 2.7C.8 4.8 3.5 8 3.5 8s2.7-3.2 2.7-5.3A2.7 2.7 0 0 0 3.5 0zm0 3.8a1 1 0 1 1 0-2 1 1 0 0 1 0 2z" fill="#fff"/></svg></span>
        <span>4817 Thistlewood Lane Cary<br>NC 27604</span></li>
      <li><span class="icon"><svg width="7" height="7" viewBox="0 0 7 7"><path d="M1.4 0l1.2 1.6-.6.9c.4.9 1 1.5 1.9 1.9l.9-.6L6.4 5 5.7 6.4C2.8 6.2.6 4 .4 1.1z" fill="#fff"/></svg></span>
        <span>Cell : 919-555-0148</span></li>
      <li><span class="icon"><svg width="8" height="6" viewBox="0 0 8 6"><rect x=".5" y=".5" width="7" height="5" fill="none" stroke="#fff"/><path d="M.5.5L4 3.3 7.5.5" fill="none" stroke="#fff"/></svg></span>
        <span>marion@brennickquality.example</span></li>
      <li><span class="icon"><svg width="8" height="8" viewBox="0 0 8 8"><circle cx="4" cy="4" r="3.4" fill="none" stroke="#fff" stroke-width=".9"/><path d="M.6 4h6.8M4 .6c-1.8 2-1.8 4.8 0 6.8M4 .6c1.8 2 1.8 4.8 0 6.8" fill="none" stroke="#fff" stroke-width=".7"/></svg></span>
        <span>www.brennickquality.example</span></li>
    </ul>
  </section>

  <section class="card card--back">
    <svg class="decor" width="458" height="230" viewBox="0 0 458 230">
      <path d="M0 0 L70 0 C62 30 80 50 52 70 C30 86 28 100 0 110 Z" fill="var(--orange)"/>
      <path d="M0 0 L58 0 C50 28 66 46 42 63 C22 77 20 90 0 98 Z" fill="var(--teal)"/>
      <path d="M458 230 L388 230 C396 200 378 180 406 160 C428 144 430 130 458 120 Z" fill="var(--orange)"/>
      <path d="M458 230 L400 230 C408 202 392 184 416 167 C436 153 438 140 458 132 Z" fill="var(--teal)"/>
    </svg>
    <div class="brand">
      <span class="brand__dot"></span>
      <span class="brand__name">Brennick Quality Solutions</span>
    </div>
  </section>
</body>
</html>
```